National Intensive Course Provider needs an advert designed to appear in trams

We need an advertisement designed to put in trams, the dimensions are 660mm wide and 203mm height. We offer intensive driving courses all over the UK, allowing pupils to complete a full driving course within a week/two weeks with both the theory and practical tests included in the course (as required). We would like the colours used to be green and dark blue, maybe red also, whatever looks best from them colours really.

Key Points to highlight:
- Pass your driving test within 1 week
- Start your course as early as next week
- Both tests included as part of your course (if required)

I have attached some images which could be included in the design

```html
<!DOCTYPE html>
<html lang="en">
<head>
<meta charset="utf-8">
<title>Intensive Driving Courses – Tram Advert</title>
<link rel="stylesheet" href="https://fonts.googleapis.com/css2?family=Roboto:wght@500;700;900&display=swap">
<style>
  :root {
    --navy: #0c0f40;
    --red: #e3111c;
    --silver: #cfd0d4;
    --white: #ffffff;
    --backdrop: #ececec;
    --photo-sky: #b9d3e6;
    --photo-green: #6f8f4e;
    --photo-road: #b7aa98;
  }
  * { box-sizing: border-box; margin: 0; padding: 0; }
  html, body { width: 1200px; height: 514px; overflow: hidden; background: var(--backdrop); }
  .canvas { position: relative; width: 1200px; height: 514px; overflow: hidden; background: var(--backdrop); }
  .advert {
    position: absolute; left: 0; top: 72px; width: 1200px; height: 370px;
    overflow: hidden; font-family: "Roboto", Arial, sans-serif; color: var(--white);
  }
  .advert-shapes { position: absolute; inset: 0; width: 100%; height: 100%; display: block; }
  .brand-name {
    position: absolute; left: 588px; top: 36px;
    font-size: 42px; font-weight: 900; line-height: 1; letter-spacing: 1px; color: var(--white);
    white-space: nowrap;
  }
  .headline { position: absolute; right: 39px; line-height: 1; font-weight: 700; text-align: right; white-space: nowrap; }
  .headline--offer { top: 33px; font-size: 48px; }
  .headline--course { font-size: 37px; color: var(--red); }
  .headline--course-1 { top: 83px; }
  .headline--course-2 { top: 115px; }
  .headline--region { top: 152px; font-size: 51px; }
  .headline--region .accent { color: var(--red); }
  .benefit {
    position: absolute; right: 39px; font-size: 22px; font-weight: 500; line-height: 1;
    text-align: right; white-space: nowrap;
  }
  .benefit .tick { display: inline-block; width: 18px; height: 16px; margin-right: 10px; vertical-align: -1px; }
  .benefit--1 { top: 221px; }
  .benefit--2 { top: 255px; }
  .benefit--3 { top: 289px; }
  .benefit--4 { top: 316px; }
</style>
</head>
<body>
<div class="canvas">
  <section class="advert">
    <svg class="advert-shapes" viewBox="0 0 1248 385" preserveAspectRatio="none" xmlns="http://www.w3.org/2000/svg">
      <defs>
        <linearGradient id="mainPhotoTone" x1="0" y1="0" x2="0" y2="1">
          <stop offset="0" stop-color="#b9d3e6"/>
          <stop offset="0.35" stop-color="#6f8f4e"/>
          <stop offset="0.7" stop-color="#b7aa98"/>
          <stop offset="1" stop-color="#8d8f96"/>
        </linearGradient>
        <linearGradient id="insetPhotoTone" x1="0" y1="0" x2="0" y2="1">
          <stop offset="0" stop-color="#5f8a45"/>
          <stop offset="0.6" stop-color="#7b8b6a"/>
          <stop offset="1" stop-color="#c9343a"/>
        </linearGradient>
      </defs>
      <rect class="main-photo" x="0" y="0" width="820" height="385" fill="url(#mainPhotoTone)"
            role="img" aria-label="Photo: a smiling learner driver holding her licence high-fives her instructor beside a silver learner car with L plate and traffic cones"/>
      <path class="navy-panel" d="M553 0 H1248 V385 H800 C650 330 560 160 553 0 Z" fill="var(--navy)"/>
      <path class="red-swoosh" d="M471 0 H540 C548 165 640 330 790 385 H745 C600 330 490 170 471 0 Z" fill="var(--red)"/>
      <path class="silver-edge" d="M540 0 C548 165 640 330 790 385 H800 C650 330 560 160 553 0 Z" fill="var(--silver)"/>
      <circle class="inset-frame" cx="623" cy="275" r="102" fill="var(--silver)"/>
      <circle class="inset-photo" cx="623" cy="275" r="90" fill="url(#insetPhotoTone)"
              role="img" aria-label="Photo: a happy pupil holding a pass certificate in front of a red car"/>
    </svg>

    <div class="brand-name">KESTRAVO</div>

    <div class="headline headline--offer">WE OFFER</div>
    <div class="headline headline--course headline--course-1">INTENSIVE DRIVING</div>
    <div class="headline headline--course headline--course-2">COURSES</div>
    <div class="headline headline--region">ALL OVER THE <span class="accent">UK</span></div>

    <p class="benefit benefit--1"><svg class="tick" viewBox="0 0 18 16" aria-hidden="true"><path d="M1 9 L6 14 L17 1" fill="none" stroke="var(--red)" stroke-width="2.4"/></svg>Pass your driving test within 1 week</p>
    <p class="benefit benefit--2"><svg class="tick" viewBox="0 0 18 16" aria-hidden="true"><path d="M1 9 L6 14 L17 1" fill="none" stroke="var(--red)" stroke-width="2.4"/></svg>Start your course as early as next week</p>
    <p class="benefit benefit--3"><svg class="tick" viewBox="0 0 18 16" aria-hidden="true"><path d="M1 9 L6 14 L17 1" fill="none" stroke="var(--red)" stroke-width="2.4"/></svg>Both tests included as part of</p>
    <p class="benefit benefit--4">your course (if required)</p>
  </section>
</div>
</body>
</html>
```